Labels design for a a range of food products

We are looking for labels design for a range of food product. The design should be the same for all the label with brown/black background and gold and white wording like the one attached.
The size and the content of the label will change depending on the different products.
I have also attached the logo to be used which is the logo "VELDORA" Marsk. You shall be using the black and gold version. Brighter/shining gold is better.
The first label to be designed is the one related a plastic tray like the one Cappelletti" file: IMG_20151231_021838
The second label to be designed is the one related to a bottle like the one "Olive Oil" file; IMG_20151231_021651
The third label to be designed is the one related to a jar like the one "Olive Taggiasche" file: IMG_20151231_021531 and IMG_20151231_021549
The fourth label to be designed is the one related to bag like the one IMG_20151231_021506
The fifth label to be designed is the one related to the bottle. IMG_20151231_021426_panorama
This files are only samples. I have attached a file excel "Texts for Labels" in which you will find the text to be applied for the labels.
In order to decide the best design a front and a back label should be provided.

Food Consumers

Product

• Front and Back Label
• Some pictures of the product on the label would be nice to have to recall what is inside.

```html
<!DOCTYPE html>
<html lang="it">
<head>
<meta charset="utf-8">
<title>Aceto Balsamico di Modena IGP – Etichetta</title>
<link rel="stylesheet" href="https://fonts.googleapis.com/css2?family=Dancing+Script:wght@700&display=swap">
<style>
  :root {
    --canvas: #e9e9e9;
    --label-dark: #0b0b0b;
    --label-mid: #2a2a2a;
    --arc-grey: #5a5a5a;
    --leaf-grey: #6e6e6e;
    --gold: #d4a437;
    --gold-light: #f3d27a;
    --white: #ffffff;
    --seal-blue: #1f3f99;
    --seal-yellow: #f2d21b;
  }
  * { margin: 0; padding: 0; box-sizing: border-box; }
  html, body { width: 1200px; height: 1200px; overflow: hidden; }
  body {
    background: radial-gradient(circle at 50% 30%, #ffffff 0%, var(--canvas) 70%);
    display: flex; align-items: center; justify-content: center;
    font-family: "Dancing Script", cursive;
  }
  .label {
    position: relative;
    width: 820px; height: 1024px;
    border-radius: 28px;
    overflow: hidden;
    background: radial-gradient(ellipse at 55% 40%, var(--label-mid) 0%, var(--label-dark) 65%);
    box-shadow: 0 10px 30px rgba(0,0,0,.25);
  }
  .label__decor { position: absolute; inset: 0; }
  .label__leaves {
    position: absolute; left: 40px; right: 40px; top: 300px; bottom: 0;
    background: radial-gradient(ellipse at 50% 60%, rgba(110,110,110,.55) 0%, rgba(90,90,90,.25) 50%, rgba(0,0,0,0) 75%);
  }
  .brand {
    position: absolute; top: 95px; left: 0; right: 0;
    display: flex; flex-direction: column; align-items: center;
  }
  .brand__ring {
    width: 300px; height: 300px; border-radius: 50%;
    border: 14px solid var(--gold);
    box-shadow: inset 0 0 0 2px var(--gold-light);
  }
  .brand__name {
    margin-top: 8px;
    font-size: 62px; line-height: 1;
    color: var(--gold);
    text-align: center;
  }
  .product {
    position: absolute; top: 520px; left: 0; right: 0;
    text-align: center;
  }
  .product__title {
    color: var(--white);
    font-size: 88px; line-height: 86px;
  }
  .product__aging {
    color: var(--gold);
    font-size: 60px; line-height: 1.2;
  }
  .volume {
    position: absolute; left: 98px; top: 860px;
    color: var(--white);
    font-size: 68px;
  }
  .seal {
    position: absolute; left: 590px; top: 790px;
    width: 152px; height: 152px; border-radius: 50%;
    background: var(--seal-blue);
    border: 10px solid var(--seal-yellow);
  }
</style>
</head>
<body>
  <main class="label">
    <svg class="label__decor" viewBox="0 0 820 1024" aria-hidden="true">
      <path d="M -40 700 Q 60 200 520 0" fill="none" stroke="var(--arc-grey)" stroke-width="70" opacity=".8"/>
      <path d="M 900 120 Q 760 60 620 0" fill="none" stroke="var(--arc-grey)" stroke-width="40" opacity=".4"/>
    </svg>
    <div class="label__leaves" role="img" aria-label="Decorative grey wheat leaves rising behind the text"></div>

    <header class="brand">
      <div class="brand__ring"></div>
      <p class="brand__name">"VELDORA" Marsk</p>
    </header>

    <section class="product">
      <h1 class="product__title">Aceto Balsamico<br>di Modena IGP</h1>
      <p class="product__aging">invecchiato</p>
    </section>

    <p class="volume">250ml ℮</p>
    <div class="seal" role="img" aria-label="Protected geographical indication seal"></div>
  </main>
</body>
</html>
```